Real Estate Sales Brokerage

Design a modern and fresh looking standard size business card, incorporate our logo's color scheme and modern appearance with head shot photo on front side and incorporate our log on the back side

Target Market(s)

Residential Home sales

Industry/Entity Type

Real Estate Agent

Font styles to use
Sans Serif

Colors

Designer to choose colors to be used in the design.

Requirements
Must have
• fresh, modern, not too busy, incorporate head shot in front of the card, incorporate logo in front and back of the card. Use logo design scheme as appropriate.
Nice to have
• horizontal and vertical options to compare would be nice.

```html
<!DOCTYPE html>
<html lang="en">
<head>
<meta charset="utf-8">
<title>Harbor Crest Realty – Business Card</title>
<link href="https://fonts.googleapis.com/css2?family=Open+Sans:wght@400;600;700&display=swap" rel="stylesheet">
<style>
  :root {
    --backdrop: #111111;
    --card-white: #ffffff;
    --olive: #696739;
    --olive-dark: #4f4d26;
    --sun: #f2d24b;
    --photo-blue: #5d7790;
    --photo-skin: #c9a58a;
  }
  * { box-sizing: border-box; margin: 0; padding: 0; }
  html, body {
    width: 1200px; height: 1000px; overflow: hidden;
    background: var(--backdrop);
    font-family: "Open Sans", Arial, sans-serif;
  }
  .card {
    position: absolute;
    width: 540px; height: 320px;
    border-radius: 22px;
    overflow: hidden;
  }
  .card--front { left: 40px; top: 170px; background: var(--card-white); }
  .card--back  { left: 620px; top: 500px; background: var(--olive); }

  .card__geometry { position: absolute; inset: 0; }

  .agent { position: absolute; left: 36px; top: 30px; color: var(--olive-dark); }
  .agent__name { font-size: 21px; font-weight: 700; letter-spacing: .5px; line-height: 1.3; }
  .agent__title { font-size: 14px; font-weight: 400; line-height: 1.3; }
  .agent__contact { margin-top: 14px; font-size: 12.5px; line-height: 1.55; }

  .brand-mark {
    position: absolute; left: 36px; top: 190px;
    display: flex; align-items: center; gap: 10px;
  }
  .brand-mark__square { width: 26px; height: 26px; background: var(--sun); flex: none; }
  .brand-mark__name {
    font-size: 12px; font-weight: 600; line-height: 1.2;
    color: var(--olive-dark); text-transform: uppercase;
  }

  .headshot {
    position: absolute; left: 338px; top: 148px;
    width: 166px; height: 96px;
    background: linear-gradient(135deg, var(--photo-blue), var(--photo-skin) 60%, var(--photo-blue));
  }

  .back-brand {
    position: absolute; inset: 0;
    display: flex; align-items: center; justify-content: center; gap: 22px;
  }
  .back-brand__square { width: 70px; height: 70px; background: var(--sun); }
  .back-brand__name {
    font-size: 30px; font-weight: 400; line-height: 1.05;
    color: var(--card-white); text-transform: uppercase; letter-spacing: 1px;
  }
</style>
</head>
<body>
  <section class="card card--front" aria-label="Business card front">
    <svg class="card__geometry" width="540" height="320" viewBox="0 0 540 320" aria-hidden="true">
      <rect x="170" y="168" width="150" height="84" fill="var(--sun)"/>
      <rect x="0" y="266" width="320" height="54" fill="var(--olive)"/>
      <rect x="338" y="258" width="202" height="62" fill="var(--sun)"/>
    </svg>

    <div class="agent">
      <h1 class="agent__name">LOREM IPSUM</h1>
      <p class="agent__title">Director</p>
      <p class="agent__contact">123 456 789<br>email_add@domain.com<br>HarborCrestRealty.com</p>
    </div>

    <div class="headshot" role="img" aria-label="Agent headshot photo"></div>

    <div class="brand-mark">
      <span class="brand-mark__square"></span>
      <span class="brand-mark__name">Harbor<br>Crest<br>Realty</span>
    </div>
  </section>

  <section class="card card--back" aria-label="Business card back">
    <div class="back-brand">
      <span class="back-brand__square"></span>
      <span class="back-brand__name">Harbor<br>Crest<br>Realty</span>
    </div>
  </section>
</body>
</html>
```